Bref créative
Business Card for Education Consulting Company
Brio Study Mentors
Simple
Marcus Delavine
President
317 Hollins Court NE
Washington DC 20019
Marcus@briostudymentors-example.com
www.briostudymentors-example.com
Looking for a simple, clean and professional business card. The logo already has the name of the company so there is no need to include again unless you feel it adds to the overall look of the card.
Here is the compnay's logo

```html
<!DOCTYPE html>
<html lang="en">
<head>
<meta charset="utf-8">
<title>Brio Study Mentors – Business Card</title>
<link rel="stylesheet" href="https://fonts.googleapis.com/css2?family=Cinzel:wght@400;600&display=swap">
<style>
  :root {
    --page: #e9e7e3;
    --card: #ffffff;
    --brand-blue: #2a5fc0;
    --stripe-grey: #8b8f96;
    --ink-light: #ffffff;
  }
  * { margin: 0; padding: 0; box-sizing: border-box; }
  html, body {
    width: 1200px; height: 914px; overflow: hidden;
    background: var(--page);
    font-family: "Cinzel", "Times New Roman", serif;
  }
  .business-card {
    position: absolute; left: 100px; top: 171px;
    width: 1000px; height: 572px;
    background: var(--card);
    box-shadow: 0 10px 30px rgba(0,0,0,0.18);
    overflow: hidden;
  }
  .card-shapes { position: absolute; inset: 0; }
  .holder {
    position: absolute; left: 46px; top: 40px;
    color: var(--ink-light);
  }
  .holder-name { font-size: 26px; font-weight: 400; letter-spacing: 1px; }
  .holder-title { font-size: 15px; margin-top: 6px; letter-spacing: 1px; }
  .contact-list {
    position: absolute; left: 46px; top: 318px;
    max-width: 380px;
    list-style: none; color: var(--ink-light);
    font-size: 14px; letter-spacing: 0;
  }
  .contact-item { display: flex; align-items: flex-start; gap: 10px; margin-bottom: 10px; }
  .contact-icon {
    flex: 0 0 22px; width: 22px; height: 22px;
    border-radius: 50%; background: var(--ink-light);
    display: flex; align-items: center; justify-content: center;
  }
  .contact-text { line-height: 22px; white-space: nowrap; }
  .brand-mark {
    position: absolute; left: 590px; top: 238px;
    display: flex; align-items: center; gap: 18px;
    color: var(--brand-blue);
  }
  .brand-dot {
    width: 54px; height: 54px; border-radius: 50%;
    background: var(--brand-blue);
  }
  .brand-name {
    font-size: 36px; font-weight: 600; line-height: 1.1; letter-spacing: 1px;
  }
</style>
</head>
<body>
  <div class="business-card">
    <svg class="card-shapes" width="1000" height="572" viewBox="0 0 1000 572">
      <path class="grey-stripe" d="M0 0 H592 C560 170 480 330 432 572 H0 Z" fill="var(--stripe-grey)"/>
      <path class="white-gap" d="M0 0 H576 C544 170 464 330 416 572 H0 Z" fill="var(--card)"/>
      <path class="blue-panel" d="M0 0 H566 C534 170 454 330 406 572 H0 Z" fill="var(--brand-blue)"/>
    </svg>

    <div class="holder">
      <div class="holder-name">Marcus Delavine</div>
      <div class="holder-title">President</div>
    </div>

    <ul class="contact-list">
      <li class="contact-item">
        <span class="contact-icon">
          <svg width="13" height="13" viewBox="0 0 14 14"><path d="M7 1a4 4 0 0 0-4 4c0 3 4 8 4 8s4-5 4-8a4 4 0 0 0-4-4zm0 5.5a1.5 1.5 0 1 1 0-3 1.5 1.5 0 0 1 0 3z" fill="var(--brand-blue)"/></svg>
        </span>
        <span class="contact-text">317 Hollins Court NE<br>Washington DC 20019</span>
      </li>
      <li class="contact-item">
        <span class="contact-icon">
          <svg width="13" height="13" viewBox="0 0 14 14"><path d="M3 1.5l2 0 1 3-1.3 1a7 7 0 0 0 3.8 3.8l1-1.3 3 1v2a1 1 0 0 1-1 1A10.5 10.5 0 0 1 2 2.5a1 1 0 0 1 1-1z" fill="var(--brand-blue)"/></svg>
        </span>
        <span class="contact-text">(202) 555-0148</span>
      </li>
      <li class="contact-item">
        <span class="contact-icon">
          <svg width="13" height="13" viewBox="0 0 14 14"><rect x="1.5" y="3" width="11" height="8" rx="1" fill="none" stroke="var(--brand-blue)" stroke-width="1.5"/><path d="M2 4l5 4 5-4" fill="none" stroke="var(--brand-blue)" stroke-width="1.5"/></svg>
        </span>
        <span class="contact-text">Marcus@briostudymentors-example.com</span>
      </li>
      <li class="contact-item">
        <span class="contact-icon">
          <svg width="13" height="13" viewBox="0 0 14 14"><circle cx="7" cy="7" r="5.5" fill="none" stroke="var(--brand-blue)" stroke-width="1.3"/><path d="M1.5 7h11M7 1.5c-2.5 3-2.5 8 0 11M7 1.5c2.5 3 2.5 8 0 11" fill="none" stroke="var(--brand-blue)" stroke-width="1.1"/></svg>
        </span>
        <span class="contact-text">www.briostudymentors-example.com</span>
      </li>
    </ul>

    <div class="brand-mark">
      <span class="brand-dot"></span>
      <span class="brand-name">Brio Study<br>Mentors</span>
    </div>
  </div>
</body>
</html>
```